Management Consulting needing a cool business card for client acquisition and networking

We are looking for a business card that is progressive and fresh that conveys innovation, forward thinking, and confidence. The business card is for a company based in Charlotte NC called, 'MERIDOX CONSULTING GROUP LLC'. The company primarily works with banks, insurance, and brokerages to implement innovative solutions to help them streamline their operations, to more effectively manage risks, and to improve their customer relationships.

Target Market(s)

Typically meet with Chief Financial Officers, Chief Information Officers, Chief Operations Officer, Business Unit Leader. The target market are generally 40-55 years, male, white, master level education plus.

Industry/Entity Type

Progressive

Font styles to use
Serif
Other font styles liked:
• Calibri

Requirements
Should not have
• Designs that look too much like law firms or accounting companies. Too conservative

```html
<!DOCTYPE html>
<html lang="en">
<head>
<meta charset="utf-8">
<title>Meridox Consulting Group – Business Card Concepts</title>
<link rel="stylesheet" href="https://fonts.googleapis.com/css2?family=Roboto+Slab:wght@400;700&family=Arimo:wght@400&display=swap">
<style>
  :root{
    --page:#ffffff;
    --ink:#ffffff;
    --cyan:#3fb6d6;
    --steel:#6b6e73;
    --tan:#c4a266;
    --tan-dark:#9d7c3d;
    --red:#c8151b;
    --brown:#4c403d;
    --grey-band:#b5b5b5;
    --black:#111111;
    --slab:"Roboto Slab", Georgia, serif;
    --sans:"Arimo", Arial, sans-serif;
  }
  *{margin:0;padding:0;box-sizing:border-box}
  html,body{width:848px;height:1200px;overflow:hidden;background:var(--page)}
  .sheet{position:relative;width:848px;height:1200px;border-left:1px solid #8a8a8a;border-bottom:1px solid #8a8a8a}
  .card{position:absolute;width:358px;height:204px;overflow:hidden;color:var(--ink);box-shadow:0 0 0 1px #cfcfcf}
  .card svg.bg{position:absolute;inset:0;width:100%;height:100%}
  .t{position:absolute;white-space:nowrap;font-family:var(--slab);font-weight:700;letter-spacing:.2px}
  .company{font-size:9.5px}
  .name{font-size:11px;font-weight:400}
  .title{font-size:7px;font-style:italic;font-weight:700}
  .contact{font-size:9.5px;line-height:14px}
  .contact.sans{font-family:var(--sans);font-weight:400;font-size:11px;line-height:14.5px;color:#e6e9ef}
  .mark{position:absolute;border:1px solid rgba(255,255,255,.85);border-radius:50%;display:flex;align-items:center;justify-content:center;font-family:var(--slab);font-weight:700;color:var(--ink)}
  .mark.sm{width:34px;height:34px;font-size:9px}
  .mark.md{width:44px;height:44px;font-size:11px}
  .mark.lg{width:60px;height:60px;font-size:15px}
</style>
</head>
<body>
<main class="sheet">

  <!-- Concept 1: chevron -->
  <section class="card" style="left:51px;top:20px">
    <svg class="bg" viewBox="0 0 358 204" preserveAspectRatio="none">
      <defs>
        <linearGradient id="c1blue" x1="0" y1="0" x2="1" y2="1"><stop offset="0" stop-color="#1d6fb8"/><stop offset=".6" stop-color="#0d2a55"/><stop offset="1" stop-color="#0a1630"/></linearGradient>
        <linearGradient id="c1grey" x1="0" y1="0" x2="1" y2="0"><stop offset="0" stop-color="#8f9194"/><stop offset="1" stop-color="#3b3e44"/></linearGradient>
      </defs>
      <rect width="358" height="204" fill="url(#c1blue)"/>
      <polygon points="0,0 168,0 264,102 168,204 0,204" fill="url(#c1grey)"/>
      <polyline points="168,0 264,102 168,204" fill="none" stroke="#5fb4ef" stroke-width="2"/>
    </svg>
    <div class="t company" style="left:16px;top:88px">MERIDOX CONSULTING GROUP LLC</div>
    <div class="mark md" style="left:268px;top:78px">MCG</div>
  </section>
  <section class="card" style="left:435px;top:20px">
    <svg class="bg" viewBox="0 0 358 204" preserveAspectRatio="none">
      <rect width="358" height="204" fill="url(#c1blue)"/>
      <polygon points="0,0 168,0 264,102 168,204 0,204" fill="url(#c1grey)"/>
      <polyline points="168,0 264,102 168,204" fill="none" stroke="#5fb4ef" stroke-width="2"/>
    </svg>
    <div class="t name" style="right:14px;top:6px;font-family:var(--sans)">DORIAN K. VALE</div>
    <div class="t title" style="right:14px;top:22px;font-weight:400;font-family:var(--sans)">President</div>
    <div class="t contact sans" style="left:18px;top:52px">1250 Larkmoor Rd., Suite 310<br>Elmridge, Nc 27991<br>O:704.555.0142<br>C:704.555.0187<br>E: Dvale@meridoxconsulting.com</div>
    <div class="mark md" style="left:268px;top:78px">MCG</div>
  </section>

  <!-- Concept 2: navy glow with tabs -->
  <section class="card" style="left:54px;top:239px">
    <svg class="bg" viewBox="0 0 358 204" preserveAspectRatio="none">
      <defs>
        <radialGradient id="c2glow" cx=".05" cy=".75" r=".9"><stop offset="0" stop-color="#2f86c8"/><stop offset=".45" stop-color="#12306a"/><stop offset="1" stop-color="#0a1434"/></radialGradient>
      </defs>
      <rect width="358" height="204" fill="url(#c2glow)"/>
      <rect x="0" y="16" width="14" height="50" fill="#0c4f66"/>
      <rect x="0" y="82" width="14" height="46" fill="var(--cyan)"/>
      <rect x="0" y="142" width="14" height="50" fill="#0c4f66"/>
      <line x1="233" y1="88" x2="233" y2="106" stroke="var(--red)" stroke-width="1.5"/>
    </svg>
    <div class="mark sm" style="left:164px;top:26px">MCG</div>
    <div class="t company" style="left:20px;top:91px">MERIDOX CONSULTING GROUP LLC</div>
    <div class="t name" style="left:240px;top:89px">DORIAN K. VALE</div>
    <div class="t title" style="left:297px;top:104px">President</div>
  </section>
  <section class="card" style="left:436px;top:239px">
    <svg class="bg" viewBox="0 0 358 204" preserveAspectRatio="none">
      <rect width="358" height="204" fill="url(#c2glow)"/>
    </svg>
    <div class="t contact" style="left:46px;top:83px">1250 Larkmoor Rd., Suite 310, Elmridge, Nc 27991<br>O:704.555.0142&nbsp;&nbsp;&nbsp;&nbsp;&nbsp;C:704.555.0187<br>E: Dvale@meridoxconsulting.com</div>
  </section>

  <!-- Concept 3: tan with band -->
  <section class="card" style="left:54px;top:463px">
    <svg class="bg" viewBox="0 0 358 204" preserveAspectRatio="none">
      <rect width="358" height="204" fill="var(--tan)"/>
      <rect width="130" height="204" fill="var(--tan-dark)"/>
      <rect x="0" y="0" width="280" height="3" fill="var(--red)"/>
      <rect x="280" y="0" width="78" height="3" fill="var(--black)"/>
      <rect x="0" y="60" width="358" height="8" fill="var(--red)"/>
      <rect x="0" y="68" width="130" height="58" fill="var(--black)"/>
      <rect x="130" y="68" width="228" height="58" fill="var(--steel)"/>
      <rect x="0" y="126" width="358" height="8" fill="var(--red)"/>
      <rect x="0" y="200" width="80" height="4" fill="var(--black)"/>
      <rect x="80" y="200" width="278" height="4" fill="var(--red)"/>
    </svg>
    <div class="mark sm" style="left:48px;top:80px">MCG</div>
    <div class="t company" style="left:136px;top:91px">MERIDOX CONSULTING GROUP LLC</div>
  </section>
  <section class="card" style="left:436px;top:463px">
    <svg class="bg" viewBox="0 0 358 204" preserveAspectRatio="none">
      <rect width="358" height="204" fill="var(--tan)"/>
      <rect width="130" height="204" fill="var(--tan-dark)"/>
      <rect x="0" y="0" width="300" height="3" fill="var(--red)"/>
      <rect x="300" y="0" width="58" height="3" fill="var(--black)"/>
      <rect x="0" y="60" width="358" height="8" fill="var(--red)"/>
      <rect x="0" y="68" width="130" height="58" fill="var(--black)"/>
      <rect x="130" y="68" width="228" height="58" fill="var(--steel)"/>
      <rect x="0" y="126" width="358" height="8" fill="var(--red)"/>
      <rect x="0" y="200" width="80" height="4" fill="var(--black)"/>
      <rect x="80" y="200" width="278" height="4" fill="var(--red)"/>
    </svg>
    <div class="t name" style="left:14px;top:84px">DORIAN K. VALE</div>
    <div class="t title" style="left:64px;top:100px">President</div>
    <div class="t contact" style="left:136px;top:68px;font-size:10px">1250 Larkmoor Rd., Suite 310,<br>Elmridge, Nc 27991<br>O:704.555.0142&nbsp;&nbsp;&nbsp;C:704.555.0187<br>E: Dvale@meridoxconsulting.com</div>
  </section>

  <!-- Concept 4: brown with red band -->
  <section class="card" style="left:60px;top:701px">
    <svg class="bg" viewBox="0 0 358 204" preserveAspectRatio="none">
      <rect width="358" height="204" fill="var(--brown)"/>
      <rect x="0" y="115" width="358" height="20" fill="var(--red)"/>
      <rect x="0" y="135" width="358" height="18" fill="var(--grey-band)"/>
    </svg>
    <div class="mark lg" style="left:50px;top:34px">MCG</div>
    <div class="t company" style="left:136px;top:58px">MERIDOX CONSULTING GROUP LLC</div>
    <div class="t name" style="left:28px;top:117px;font-size:14px;font-family:var(--sans)">DORIAN K. VALE</div>
    <div class="t title" style="left:66px;top:140px">President</div>
  </section>
  <section class="card" style="left:443px;top:701px">
    <svg class="bg" viewBox="0 0 358 204" preserveAspectRatio="none">
      <rect width="358" height="204" fill="var(--brown)"/>
      <rect x="0" y="114" width="358" height="17" fill="var(--grey-band)"/>
      <rect x="0" y="131" width="358" height="73" fill="var(--red)"/>
    </svg>
    <div class="mark lg" style="left:50px;top:34px">MCG</div>
    <div class="t company" style="left:136px;top:58px">MERIDOX CONSULTING GROUP LLC</div>
    <div class="t contact" style="left:42px;top:143px">1250 Larkmoor Rd., Suite 310, Elmridge, Nc 27991<br>O:704.555.0142&nbsp;&nbsp;&nbsp;&nbsp;&nbsp;C:704.555.0187<br>E: Dvale@meridoxconsulting.com</div>
  </section>

  <!-- Concept 5: navy diagonals -->
  <section class="card" style="left:60px;top:925px">
    <svg class="bg" viewBox="0 0 358 204" preserveAspectRatio="none">
      <defs>
        <linearGradient id="c5navy" x1="0" y1="0" x2="1" y2="1"><stop offset="0" stop-color="#14285e"/><stop offset="1" stop-color="#0b1740"/></linearGradient>
      </defs>
      <rect width="358" height="204" fill="url(#c5navy)"/>
      <polygon points="60,204 190,0 240,0 110,204" fill="#ffffff" opacity=".04"/>
      <polygon points="170,204 300,0 330,0 200,204" fill="#000000" opacity=".12"/>
      <polygon points="0,120 76,0 100,0 0,160" fill="#ffffff" opacity=".04"/>
      <line x1="0" y1="63" x2="358" y2="63" stroke="var(--red)" stroke-width="2"/>
    </svg>
    <div class="mark sm" style="left:18px;top:26px">MCG</div>
    <div class="t company" style="left:98px;top:38px">MERIDOX CONSULTING GROUP LLC</div>
    <div class="t name" style="left:118px;top:104px">DORIAN K. VALE</div>
    <div class="t title" style="left:186px;top:120px">President</div>
  </section>
  <section class="card" style="left:443px;top:925px">
    <svg class="bg" viewBox="0 0 358 204" preserveAspectRatio="none">
      <rect width="358" height="204" fill="url(#c5navy)"/>
      <polygon points="60,204 190,0 240,0 110,204" fill="#ffffff" opacity=".04"/>
      <polygon points="170,204 300,0 330,0 200,204" fill="#000000" opacity=".12"/>
      <polygon points="0,120 76,0 100,0 0,160" fill="#ffffff" opacity=".04"/>
      <line x1="0" y1="63" x2="358" y2="63" stroke="var(--red)" stroke-width="2"/>
    </svg>
    <div class="mark sm" style="left:18px;top:26px">MCG</div>
    <div class="t company" style="left:98px;top:38px">MERIDOX CONSULTING GROUP LLC</div>
    <div class="t contact" style="left:32px;top:92px;text-align:center;width:294px">1250 Larkmoor Rd., Suite 310, Elmridge, Nc 27991<br>O:704.555.0142&nbsp;&nbsp;&nbsp;&nbsp;&nbsp;C:704.555.0187<br>E: Dvale@meridoxconsulting.com</div>
  </section>

</main>
</body>
</html>
```